Cloud Hosting Startup, and Panthers!

Hi!

We are quillbarrow.com

A new hosting service that aims to provide awesome hosting and a bit of development work for free to get people set up.

We have decided on a logo and a theme. Awesome Panthers.

So, we are all about Panthers =)

-

We greatly desire a super super cool vector scene for the homepage. We love mountains, blue mountains, and green grass. Panthers hiding in long grass or leaping through the air to accentuate the coolness of our service would also be most appreciated.

Panthers hiding amongst crisp blue mountains, or hanging out on snowy mountain peaks thinking Panther things.

Or in green grassy jungles, hiding next to rocks and scaring zebras.

Or something =)

-

For the sub pages we would just like a style guide, showing the standard h1,h2's and some other items for layout.

As you can see at quillbarrow.com we are almost ready for launch, we are web developers ourselves, and so we got the site design as far as we could.

We have our software written and ready for customers, however the site just doesn't tell you what its about from a glance! That's why we need you. So, Panthers, Cool cool, sweet Panthers to accentuate our cool new launch and hosting service.

We have included the vectors used and the site design as it stands. We would like to remain with the three items 'mini-panther', 'standard panther', and 'epic panther' from this page: quillbarrow.com/signup

Apart from the epic panthers, and some variation of the panthers used for the logo, we are not fully attached other elements. We have gone with a strong red white and black, but we are just wacky developers, we need your help!

Looking forward to some great designs! If you are inspired by Panthers and super cool web hosting, this project is for you.

Thanks!!

The Quillbarrow.com Team
Updates

Project payment has been guaranteed, we are committed to a result

Just a quick update based on a designer question:

We have spent many weeks of drinking coffee and coding, we have finished all the coding, all done!

If you take a look at Quillbarrow.com you can see the result.

Basically we are looking for someone to take what we have already done (files attached of all our work) and make it less like a developer designed it, which is what happened along the way =)

Help us obi wan kenobi ..
 

Basically, we are looking for increased awesome.

We have a really cool, cheap hosting and template product offering, we would love it if someone could breathe the life of Panther into it =)

Ok,

Thanks =)

Sorry, one more update =)

Basically we are not looking for an entire site re-design, the major thing is a cool scene for the homepage with panthers and mountains =)

We are just looking for a touch up, a polish, someone to give it the design magic that communicates the message in the copy we have written. We have worked out our product and completed it, we just need someone to help us bring it to the market.

Ok, thanks!

One final update then we will return to coding our Panther and leave you all alone =)

Our internet heroes are: http://www.vantorix.com/

We love them, their purple colour scheme makes us unhappy, but we so love their signup and plan selection process.

Ok!

Thanks so much, from Quillbarrow Team

Reason: Deadline has been extended one day to allow new designers time to prepare some panther concepts. We will also use the extra day to await funds transfer to increase the budget of the project and hopefully add a 2nd place prize (pixelguild fees permitting) Thanks everyone! Marcus Quillbarrow.com

Project budget has been upgraded, and a second place payment has been added

Thanks all!

Reason: Deadline extended a further one day, 1st prize and 2nd prize payments have been updated today, looking forward to submissions! Thanks everyone

Just an update, really great designs coming in, loving all the panther concepts =)

We will award the competition on the 21st, and we have two prizes now, we will award one based on visual design and appeal (the most stunning panther), and one based on use of copy and user interface (the easiest panther)

Ok!

Thanks, hope you have enjoyed designing, we have definitely enjoyed receiving designs to bring our idea to life

Thanks!!

Marcus

Quillbarrow

Sorry!

One more update, we have added a third prize now of $100 

We love the designs too much not to make use of them =)

Ok!

Last update =)

Thanks all

Hi All,

Wonderful work, thanks everyone for feedback and revisions

We have only one day of the competition left, we are asking now for final submissions, we have provided a style guide template here:

http://quillbarrow.com/web_final_template.psd

The team will judge the competition tomorrow, we have now 3 prizes and we will add 2 participation payments as a fourth prize as we have asked some designers for some strange requests =)

Ok!

Looking forward to final submissions with the home page and style guide, thanks again!

Marcus

Quillbarrow

Target Market(s)

Tech savvy people, but not tech geniuses, young fun people who at least know what web-hosting is

Industry/Entity Type

Software

Requirements
Must have
• - super super cool vector landscape for the homepage
- some number of sub pages, in accordance with the site structure as it stands

```html
<!DOCTYPE html>
<html lang="en">
<head>
<meta charset="utf-8">
<title>Quillbarrow – Powerful, Instant Websites</title>
<link rel="stylesheet" href="https://fonts.googleapis.com/css2?family=Vollkorn:ital,wght@0,700;0,900;1,700;1,900&family=PT+Sans:wght@400;700&family=Roboto+Condensed:ital,wght@1,700&display=swap">
<style>
  :root {
    --ink: #000;
    --hero-bg: #1a1a1a;
    --hero-grey: #3b3b3d;
    --brand-red: #e2463a;
    --cta-orange: #ec5a0c;
    --sky-light: #7dd2f8;
    --sky-mid: #1f8fe8;
    --sky-deep: #0c3bb0;
    --forest: #061127;
    --footer-bg: #050b1a;
    --field: #262c37;
    --text-light: #e9f1f7;
    --green-badge: #5aa51a;
    --blue-badge: #2d7fcc;
  }
  * { box-sizing: border-box; margin: 0; padding: 0; }
  html, body { width: 1200px; height: 1154px; overflow: hidden; background: var(--ink); }
  body { position: relative; font-family: "PT Sans", sans-serif; color: var(--text-light); }

  .hero { position: absolute; left: 0; top: 0; width: 1200px; height: 560px;
    background: radial-gradient(ellipse at 30% 30%, #2a2a2a 0%, var(--hero-bg) 55%, #111 100%); }
  .topbar { position: absolute; left: 0; top: 0; width: 1200px; height: 54px; background: var(--ink); }
  .brand { position: absolute; left: 54px; top: 0; width: 194px; height: 104px; background: var(--brand-red);
    display: flex; align-items: flex-end; justify-content: center; padding-bottom: 16px;
    font: 700 20px "PT Sans", sans-serif; color: #fff; letter-spacing: .5px; }
  .nav { position: absolute; right: 38px; top: 14px; display: flex; font-size: 12px; text-transform: uppercase; }
  .nav a { color: #c9c9c9; text-decoration: none; padding: 0 15px; border-left: 1px solid #444; line-height: 22px; }
  .nav a:first-child { border-left: 0; }

  .headline { position: absolute; left: 148px; top: 150px; width: 440px; font-family: "Vollkorn", serif;
    color: var(--hero-grey); text-align: left; line-height: .9; }
  .headline .l1 { display: block; font-style: italic; font-weight: 700; font-size: 50px; padding-left: 66px; }
  .headline .l2 { display: block; font-weight: 900; font-size: 56px; padding-left: 66px; }
  .headline .l3 { display: block; font-weight: 900; font-size: 76px; }

  .tagline { position: absolute; left: 583px; top: 174px; width: 500px; text-align: center;
    font: italic 700 25px/32px "Vollkorn", serif; color: var(--text-light); }

  .cta { position: absolute; left: 705px; top: 279px; width: 480px; height: 63px; background: #1d1f24;
    border: 1px solid #33363c; }
  .cta h2 { position: absolute; left: 17px; top: 13px; font: 700 18px "Vollkorn", serif; color: #fff; }
  .cta p { position: absolute; left: 18px; top: 41px; font-size: 8px; color: #aab; }
  .cta a { position: absolute; left: 342px; top: 12px; width: 123px; height: 38px; background: var(--cta-orange);
    color: #fff; text-decoration: none; font: 700 13px/38px "PT Sans", sans-serif; text-align: center; letter-spacing: .5px; }

  .landscape { position: absolute; left: 0; top: 540px; width: 1200px; height: 400px;
    background: linear-gradient(180deg, var(--sky-light) 0%, #49b4f6 18%, var(--sky-mid) 35%, var(--sky-deep) 58%, #0a1d55 75%, var(--forest) 100%); }

  .step { position: absolute; border-radius: 50%; display: flex; align-items: center; justify-content: center;
    font: italic 700 27px "Vollkorn", serif; color: #fff; }
  .step::after { content: ""; position: absolute; inset: 18px; border-radius: 50%; border: 2px solid rgba(0,0,0,.18); }
  .step-hosting { left: 54px; top: 390px; width: 220px; height: 220px; background: var(--green-badge); }
  .step-template { left: 513px; top: 426px; width: 204px; height: 204px; background: var(--blue-badge); }
  .step-launch { left: 923px; top: 423px; width: 212px; height: 212px; background: var(--blue-badge); }

  .domain { position: absolute; left: 583px; top: 723px; width: 62px; height: 62px; border-radius: 50%; background: #23272e; }
  .domain-label { position: absolute; left: 648px; top: 740px; transform: rotate(-27deg); transform-origin: left center;
    font: italic 700 16px "Vollkorn", serif; color: #111; white-space: nowrap; }

  .footer { position: absolute; left: 0; top: 935px; width: 1200px; height: 219px; background: var(--footer-bg); }
  .social { position: absolute; top: 1029px; width: 54px; height: 54px; border-radius: 50%; background: #cfcfcf; border: 3px solid #888; }
  .social-a { left: 39px; } .social-b { left: 117px; }

  .links { position: absolute; top: 988px; }
  .links h3 { font: 700 15px "PT Sans", sans-serif; letter-spacing: .5px; color: #e6e6e6; margin-bottom: 12px; }
  .links ul { list-style: none; }
  .links li { font-size: 12px; color: #cfd6dd; line-height: 18.75px; padding-left: 16px; position: relative; }
  .links li::before { content: ""; position: absolute; left: 0; top: 4px; border-left: 10px solid #7f9fc4; border-top: 5px solid transparent; border-bottom: 5px solid transparent; }
  .links-main { left: 237px; } .links-refra { left: 433px; }

  .contact-icon { position: absolute; left: 877px; top: 922px; width: 73px; height: 62px; background: linear-gradient(135deg, #5fd0ef, #1f86b8); border-radius: 6px; }
  .contact-title { position: absolute; left: 962px; top: 947px; font: italic 700 20px "Roboto Condensed", sans-serif; color: #d8dde3; white-space: nowrap; }
  .field { position: absolute; background: var(--field); border-radius: 4px; }
  .field-name { left: 735px; top: 984px; width: 134px; height: 26px; }
  .field-email { left: 735px; top: 1020px; width: 134px; height: 25px; }
  .field-message { left: 884px; top: 984px; width: 276px; height: 128px; }
  .send { position: absolute; left: 738px; top: 1072px; width: 126px; height: 40px; background: #2c2c2c; color: #ddd;
    font-size: 15px; line-height: 40px; text-align: center; }

  .legal { position: absolute; left: 30px; top: 1130px; width: 1148px; border-top: 1px dashed #3a4150;
    text-align: center; font-size: 10px; font-weight: 700; color: #e0e0e0; padding-top: 5px; padding-right: 25px; }
</style>
</head>
<body>
  <header class="hero">
    <div class="topbar">
      <nav class="nav"><a href="#">Home</a><a href="#">Plans &amp; Pricing</a><a href="#">Sign Up</a><a href="#">Contact</a></nav>
    </div>
    <div class="brand">QUILLBARROW</div>
    <h1 class="headline"><span class="l1">powerful,</span><span class="l2">INSTANT</span><span class="l3">WEBSITES</span></h1>
    <p class="tagline">Template, Domain, Hosting and Email<br>package for under $20</p>
    <div class="cta">
      <h2>Create your beautiful website now.</h2>
      <p>Get started in 30 seconds. No credit card, no commitment.</p>
      <a href="#">GET STARTED</a>
    </div>
  </header>

  <div class="landscape" role="img" aria-label="Layered blue mountain ranges with snowy peaks and a dark pine forest in the foreground"></div>

  <div class="step step-hosting">Hosting</div>
  <div class="step step-template">Template</div>
  <div class="step step-launch">Launch</div>
  <div class="domain" role="img" aria-label="Globe icon"></div>
  <div class="domain-label">Domain &amp; Email</div>

  <footer class="footer"></footer>
  <span class="social social-a" aria-label="Social link"></span>
  <span class="social social-b" aria-label="Social link"></span>

  <div class="links links-main">
    <h3>QUILLBARROW</h3>
    <ul><li>Home</li><li>Plans &amp; Templates</li><li>Faqs</li><li>Plans &amp; Templates</li><li>Faqs</li></ul>
  </div>
  <div class="links links-refra">
    <h3>SITES REFRA</h3>
    <ul><li>Home</li><li>Plans &amp; Templates</li><li>Faqs</li><li>Plans &amp; Templates</li><li>Faqs</li></ul>
  </div>

  <div class="contact-icon" role="img" aria-label="Envelope mascot illustration"></div>
  <div class="contact-title">Contact Quillbarrow</div>
  <div class="field field-name"></div>
  <div class="field field-email"></div>
  <div class="field field-message"></div>
  <div class="send">Send</div>

  <div class="legal">© 2012 | Quillbarrow.com &nbsp;&nbsp;&nbsp; Terms of service | Privacy Polic</div>
</body>
</html>
```